Brasolina! Poster

I need a poster for an event to be staged in Gibraltar called Brasolina!
Brasolina! is a food festival and street party that celebrates GIbraltar's multicultural and colour community. The event has a tagline "Flavours of the Warm Bowl".
I am looking for a poster which captures the spirit of the event without being too obvious.
Updates

Because this event is rapidly approaching I would like to settle the design for the poster as soon as possible, so the earlier you post the better
thanks

I am trying to avoid a poster that looks too similar to last year's.
Red and White are Gibraltar's national colours and I would like to feature them in the design.
Brasolina! the name needs to be in Clarendon! (bold) with tight character spacing

Target Market(s)

Target market are the people of Gibraltar - Gibraltar is a british colony in southern Spain, population 30,000 - Gibraltarians are of British, Spanish, Italian (Genoa), Portugese and Moroccan extraction. Gibraltar also has large Hindu, Jewish and Moroccan Communities.

Industry/Entity Type

Events

Requirements
Must have
• Initially I am looking for an A2 design - we will use the same design themes for the website and also base a 120cm x 90cm banner on the design.
• Must have t
• "HearsayStagesLive.com" "Brasolina!" , "Flavours of the Warm Bowl", Friday June 19th 2009, Ropewalk Plaza, Starts 21.00 hrs Finishes 0100 hrs, Free Entry, Everyone Welcome, Firework and Laser Display at 22.30 hrs
• My company logo, Office of Heritage Bloom Fair Logo
• Title must use Clarendon font
Nice to have
• Could be a photo or an illustration nothing that too obviously reflects the theme, doesn''t need to have all or anymore than one of the main Gibraltarian cultures
Should not have
• picture of the ROck of Gibaltar, Money, bad photography in particular bad food photography, just a picture of some food

```html
<!DOCTYPE html>
<html lang="en">
<head>
<meta charset="utf-8">
<title>Brasolina! Poster</title>
<link rel="stylesheet" href="https://fonts.googleapis.com/css2?family=Alfa+Slab+One&family=Arimo:wght@700&family=Roboto+Condensed:wght@700&display=swap">
<style>
  :root {
    --crimson: #9a0000;
    --crimson-deep: #8a0000;
    --ember: #c92a0a;
    --amber: #e8860f;
    --gold: #f3c21c;
    --white: #ffffff;
    --ink: #111111;
    --plate-light: #f4ece0;
    --plate-wine: #b0473a;
  }
  html, body {
    margin: 0;
    padding: 0;
    width: 1200px;
    height: 849px;
    overflow: hidden;
    background: var(--crimson);
  }
  .poster {
    position: relative;
    width: 1200px;
    height: 849px;
    overflow: hidden;
    background:
      radial-gradient(ellipse 620px 360px at 0% 100%, var(--gold) 0%, var(--amber) 35%, rgba(201,42,10,0.6) 65%, rgba(154,0,0,0) 100%),
      linear-gradient(180deg, var(--crimson) 0%, var(--crimson-deep) 60%, var(--ember) 100%);
    font-family: 'Arimo', Arial, sans-serif;
    color: var(--white);
  }
  .site-address {
    position: absolute;
    left: 63px;
    top: 62px;
    margin: 0;
    font-size: 33px;
    font-weight: 700;
    letter-spacing: 4px;
  }
  .event-title {
    position: absolute;
    left: 150px;
    top: 98px;
    margin: 0;
    font-family: 'Alfa Slab One', 'Rockwell', serif;
    font-weight: 400;
    font-size: 130px;
    line-height: 1;
    letter-spacing: -2px;
  }
  .tagline {
    position: absolute;
    left: 522px;
    top: 252px;
    margin: 0;
    font-family: 'Roboto Condensed', 'Arial Narrow', sans-serif;
    font-size: 52px;
    font-weight: 700;
    letter-spacing: -0.5px;
  }
  .tagline-rule {
    position: absolute;
    left: 600px;
    top: 328px;
    width: 280px;
    height: 24px;
  }
  .food-visual {
    position: absolute;
    left: 90px;
    top: 262px;
    width: 440px;
    height: 460px;
    border-radius: 120px 160px 140px 60px;
    background:
      radial-gradient(circle at 62% 40%, #c9d67a 0%, rgba(201,214,122,0) 28%),
      radial-gradient(circle at 25% 35%, var(--plate-wine) 0%, rgba(176,71,58,0) 30%),
      linear-gradient(160deg, var(--white) 0%, var(--plate-light) 55%, #e3c9a4 100%);
  }
  .event-details {
    position: absolute;
    left: 520px;
    top: 418px;
    width: 640px;
    margin: 0;
    text-align: center;
    font-size: 25px;
    font-weight: 700;
    line-height: 32px;
  }
  .event-details p { margin: 0; }
  .fair-mark {
    position: absolute;
    left: 760px;
    top: 574px;
    margin: 0;
    color: var(--ink);
    font-family: 'Arimo', Arial, sans-serif;
    font-weight: 700;
    font-size: 38px;
    line-height: 42px;
    letter-spacing: 1px;
  }
  .promoter-mark {
    position: absolute;
    left: 760px;
    top: 706px;
    margin: 0;
    display: flex;
    align-items: center;
    gap: 14px;
    color: var(--ink);
    font-family: 'Arimo', Arial, sans-serif;
    font-weight: 700;
    font-size: 26px;
    line-height: 32px;
    letter-spacing: 5px;
  }
  .promoter-dot {
    width: 30px;
    height: 30px;
    border-radius: 50%;
    background: var(--ink);
    flex: none;
  }
</style>
</head>
<body>
  <main class="poster">
    <p class="site-address">HearsayStagesLive.com</p>
    <h1 class="event-title">Brasolina!</h1>
    <h2 class="tagline">Flavours of the Warm Bowl</h2>
    <svg class="tagline-rule" viewBox="0 0 280 24" aria-hidden="true">
      <line x1="10" y1="12" x2="125" y2="12" stroke="#ffffff" stroke-width="3" stroke-linecap="round"/>
      <line x1="155" y1="12" x2="270" y2="12" stroke="#ffffff" stroke-width="3" stroke-linecap="round"/>
      <circle cx="140" cy="12" r="6" fill="#ffffff"/>
    </svg>

    <div class="food-visual" role="img" aria-label="Still life of red wine, green grapes, olives, melon and bread on a white table-setting frame"></div>

    <section class="event-details">
      <p>Friday June 19th 2009, Ropewalk Plaza</p>
      <p>Starts 21.00 hrs Finishes 0100 hrs</p>
      <p>Free Entry, Everyone Welcome</p>
      <p>Firework and Laser Display at 22.30 hrs</p>
    </section>

    <p class="fair-mark">Office of Heritage<br>Bloom Fair</p>

    <p class="promoter-mark"><span class="promoter-dot"></span>HEARSAY STAGES</p>
  </main>
</body>
</html>
```